Redesign Of Current Landing Page

I need to redesign this landing page https://www.bluewillowpromos.example/?page=landing&landing=23 (Please do not opt in because when you do it will show you the home page. Please clear your cookies before going to this url above to view the 1 page landing page.)

Please use my updated website as a reference for colors and logo.
http://sitecraftorly.example/dh/bwpg/index.html

I would like the call to action to be a button that opens into a lead form...

Button would be "Download Samples"

Target Market(s)

small business owners

Industry/Entity Type

Marketing

Number of Pages Required

1 page

Colors

Designer to choose colors to be used in the design.

Requirements
Must have
• must be full responsive on all devices
Nice to have
• must have a legitimate professional apeal to it
Should not have
• open

```html
<!DOCTYPE html>
<html lang="en">
<head>
<meta charset="utf-8">
<title>Blue Willow Promos – Attract More Customers</title>
<link rel="stylesheet" href="https://fonts.googleapis.com/css2?family=Homenaje&family=Lato:wght@300;400;700&display=swap">
<style>
  :root {
    --orange: #f7923a;
    --sky: #80d8f7;
    --sky-text: #7fd3f3;
    --brand-blue: #1a78bd;
    --panel: rgba(44, 56, 66, 0.72);
    --form-box: #2e3a44;
    --ink: #3a4650;
    --grey-text: #6f7780;
    --footer: #c8c8c8;
    --white: #ffffff;
  }
  * { box-sizing: border-box; margin: 0; padding: 0; }
  html, body { width: 1200px; height: 2397px; overflow: hidden; }
  body { position: relative; font-family: "Lato", sans-serif; color: var(--ink); background: var(--white); }
  .abs { position: absolute; }
  .display { font-family: "Homenaje", sans-serif; font-weight: 400; letter-spacing: 2px; white-space: nowrap; }
  .condensed { display: inline-block; transform: scaleX(0.84); transform-origin: left top; }
  .condensed-center { transform: scaleX(0.84); transform-origin: center top; }

  /* Hero */
  .hero { left: 0; top: 0; width: 1200px; height: 887px; overflow: hidden; }
  .hero-photo { position: absolute; inset: 0;
    background:
      radial-gradient(ellipse 260px 420px at 240px 420px, rgba(240,130,40,0.55), transparent 70%),
      radial-gradient(ellipse 600px 220px at 420px 760px, rgba(230,224,214,0.9), transparent 75%),
      linear-gradient(180deg, #f3f3f1 0%, #ecebe8 55%, #e4e1dc 100%); }
  .brand { left: 671px; top: 152px; display: flex; align-items: center; gap: 12px; }
  .brand-mark { width: 34px; height: 34px; background: var(--brand-blue); }
  .brand-name { font-size: 30px; font-weight: 700; color: var(--brand-blue); letter-spacing: 1px; }
  .hero-panel { left: 412px; top: 292px; width: 747px; height: 523px; background: var(--panel); border-radius: 6px; }
  .headline { left: 443px; top: 330px; color: var(--orange); font-size: 80px; line-height: 84px; letter-spacing: 4px;
              transform: scaleX(0.78); transform-origin: left top; }
  .subhead { left: 443px; top: 528px; color: var(--white); font-size: 30px; line-height: 38px; font-weight: 300; letter-spacing: 1px; }

  .lead-form { color: var(--white); }
  .lead-form label { position: absolute; font-size: 22px; font-weight: 300; }
  .lead-form .field { position: absolute; background: var(--white); border: 0; }
  .btn { position: absolute; border: 2px solid var(--sky); border-radius: 8px; color: var(--sky);
         font-size: 17px; display: flex; align-items: center; justify-content: center; letter-spacing: 0.5px; }

  .hero-form { left: 842px; top: 324px; width: 291px; height: 470px; background: var(--form-box); border-radius: 5px; }
  .hero-form h2 { position: absolute; left: 25px; top: 18px; font-size: 37px; color: var(--sky-text); }
  .hero-form p { position: absolute; left: 25px; top: 68px; width: 232px; font-size: 18.5px; line-height: 24.5px; font-weight: 300; color: #dfe6ea; }

  /* Intro */
  .intro-col { width: 500px; }
  .intro-col h2 { font-size: 38px; margin-bottom: 14px; }
  .intro-col p { font-size: 12px; line-height: 15px; color: var(--grey-text); margin-bottom: 13px; }

  /* Benefits */
  .benefits { left: 0; top: 1171px; width: 1200px; height: 510px; background: var(--sky); }
  .benefits h2 { position: absolute; width: 100%; top: 40px; text-align: center; font-size: 38px; color: var(--ink); }
  .benefit { position: absolute; width: 300px; text-align: center; }
  .benefit svg { display: block; margin: 0 auto; }
  .benefit span { display: block; font-size: 15.5px; line-height: 19px; color: #4a5a66; margin-top: 14px; }

  /* Testimonial */
  .testimonial p { left: 144px; top: 1828px; width: 985px; font-size: 15.5px; line-height: 19px; color: #8a9098; font-weight: 300; }
  .author { left: 144px; top: 1922px; font-size: 21px; font-weight: 700; color: var(--brand-blue); }
  .place { left: 144px; top: 1949px; font-size: 21px; font-weight: 300; color: var(--sky-text); }

  /* Bottom form */
  .bottom-form { left: 0; top: 2005px; width: 1200px; height: 336px; background: var(--brand-blue); }
  .bottom-form h2 { position: absolute; width: 100%; top: 22px; text-align: center; font-size: 38px; color: var(--white); }
  .bottom-form p { position: absolute; width: 100%; top: 80px; text-align: center; font-size: 19px; color: #cfe6f6; font-weight: 300; letter-spacing: 0.5px; }

  .footer { left: 0; top: 2341px; width: 1200px; height: 56px; background: var(--footer);
            display: flex; align-items: center; justify-content: center; font-size: 12px; color: #4a4a4a; letter-spacing: 0.5px; }
</style>
</head>
<body>

<header class="hero abs">
  <div class="hero-photo" role="img" aria-label="Photo of a woman in an orange top sitting on a light sofa working on a laptop"></div>
</header>

<div class="brand abs">
  <div class="brand-mark"></div>
  <div class="brand-name">BLUE WILLOW PROMOS</div>
</div>

<div class="hero-panel abs"></div>
<h1 class="headline display abs">ATTRACT MORE<br>CUSTOMERS</h1>
<p class="subhead abs">WHO SPEND<br>MORE MONEY<br>ON YOUR BUSINESS<br>MORE OFTEN!</p>

<form class="hero-form lead-form abs">
  <h2 class="display"><span class="condensed">ENTER YOUR INFO</span></h2>
  <p>to be forwarded to our website for all the details and to receive samples in you email!</p>
  <label style="left:23px;top:193px">Name*</label>
  <div class="field" style="left:23px;top:224px;width:245px;height:29px"></div>
  <label style="left:23px;top:264px">Email*</label>
  <div class="field" style="left:23px;top:294px;width:245px;height:29px"></div>
  <label style="left:23px;top:339px">Phone*</label>
  <div class="field" style="left:23px;top:371px;width:245px;height:29px"></div>
  <div class="btn" style="left:45px;top:413px;width:203px;height:38px">Download Samples</div>
</form>

<section class="intro-col abs" style="left:42px;top:916px">
  <h2 class="display" style="color:var(--sky-text)"><span class="condensed">IMAGINE</span></h2>
  <p>being able to create exciting give away promotions that will boost your sales without ever having to worry about cost.</p>
  <p>Blue Willow Promo Group, Inc. provides high-perceived value promotional incentives to businesses that want to advertise an exciting Give Away that will instantly attract more customers from your existing advertising efforts.</p>
  <p>Your business can give away incentive certificates that are redeemable for luxury hotel &amp; resort stays with airfare included, cruises, cash for gas, groceries, dining and even electronic goods</p>
</section>

<section class="intro-col abs" style="left:654px;top:916px">
  <h2 class="display" style="color:var(--orange)"><span class="condensed">HOW CAN WE DO IT?</span></h2>
  <p>We help fill empty rooms for thousands of hotels and resorts in hundreds of destinations around the world as well as the major cruise lines. Hotels and resorts are rarely full so when we place someone in their empty rooms, they end up making it up when travelers spend money on room service, spa services, eat at their in-house restaurants, casino and take advantage of other amenities that drive revenue.</p>
  <p>We also help over 18,000 restaurants, electronic manufacturers, the major gas companies and top grocery chains in the U.S and Canada increase brand awareness as well as increase customer loyalty.</p>
</section>

<section class="benefits abs">
  <h2 class="display condensed-center">WHY OFFER INCENTIVES TO CUSTOMERS?</h2>

  <div class="benefit" style="left:150px;top:105px">
    <svg width="120" height="120" viewBox="0 0 120 120" fill="#fff">
      <rect x="8" y="4" width="7" height="112"/><rect x="8" y="109" width="108" height="7"/>
      <path d="M22 72 L48 40 L66 56 L90 20 L110 34 L110 100 L22 100 Z" opacity="0.95"/>
      <path d="M22 92 L50 66 L68 78 L110 50" stroke="#80d8f7" stroke-width="6" fill="none"/>
    </svg>
    <span>Increase Responses<br>From Your Existing Ads</span>
  </div>

  <div class="benefit" style="left:451px;top:105px">
    <svg width="120" height="120" viewBox="0 0 120 120" fill="#fff">
      <g transform="translate(60 60)">
        <rect x="-11" y="-58" width="22" height="24"/><rect x="-11" y="-58" width="22" height="24" transform="rotate(45)"/>
        <rect x="-11" y="-58" width="22" height="24" transform="rotate(90)"/><rect x="-11" y="-58" width="22" height="24" transform="rotate(135)"/>
        <rect x="-11" y="-58" width="22" height="24" transform="rotate(180)"/><rect x="-11" y="-58" width="22" height="24" transform="rotate(225)"/>
        <rect x="-11" y="-58" width="22" height="24" transform="rotate(270)"/><rect x="-11" y="-58" width="22" height="24" transform="rotate(315)"/>
        <circle r="42"/><circle r="20" fill="#80d8f7"/>
      </g>
    </svg>
    <span>#1 Sales Closing Tool -<br>Gift With Purchase</span>
  </div>

  <div class="benefit" style="left:753px;top:105px">
    <svg width="120" height="120" viewBox="0 0 120 120" fill="#fff">
      <path d="M60 4 L74 44 L116 44 L82 68 L96 112 L60 86 L24 112 L38 68 L4 44 L46 44 Z"/>
      <circle cx="60" cy="60" r="8" fill="#80d8f7"/>
    </svg>
    <span>Build Brand Awareness<br>and Trust</span>
  </div>

  <div class="benefit" style="left:150px;top:300px">
    <svg width="120" height="120" viewBox="0 0 120 120" fill="#fff">
      <path d="M38 70 L22 118 L40 108 L50 120 L60 80 Z"/><path d="M82 70 L98 118 L80 108 L70 120 L60 80 Z"/>
      <circle cx="60" cy="44" r="40"/><circle cx="60" cy="44" r="30" fill="#80d8f7"/>
      <path d="M60 24 L66 38 L80 38 L69 47 L73 61 L60 53 L47 61 L51 47 L40 38 L54 38 Z"/>
    </svg>
    <span>Insure The Sales Over<br>Your COmpetition</span>
  </div>

  <div class="benefit" style="left:451px;top:300px">
    <svg width="120" height="120" viewBox="0 0 120 120" fill="#fff">
      <rect x="4" y="14" width="112" height="92" rx="4"/>
      <rect x="16" y="26" width="88" height="68" fill="#80d8f7"/>
      <rect x="22" y="32" width="76" height="56" fill="#fff"/>
      <circle cx="60" cy="60" r="18" fill="#80d8f7"/>
    </svg>
    <span>Boost Repeat and<br>Referral Business</span>
  </div>

  <div class="benefit" style="left:753px;top:300px">
    <svg width="120" height="120" viewBox="0 0 120 120" fill="#fff">
      <path d="M60 6 C34 6 24 44 24 64 C24 80 40 90 60 90 C80 90 96 80 96 64 C96 44 86 6 60 6 Z"/>
      <path d="M10 74 C10 98 110 98 110 74 L110 84 C110 108 10 108 10 84 Z"/>
      <text x="60" y="66" text-anchor="middle" font-family="Lato, sans-serif" font-size="34" font-weight="700" fill="#80d8f7">$</text>
    </svg>
    <span>Improve Retention Rates</span>
  </div>
</section>

<section class="testimonial">
  <svg class="abs" style="left:550px;top:1712px" width="102" height="78" viewBox="0 0 102 78" fill="#f7923a">
    <circle cx="22" cy="56" r="22"/><path d="M2 56 C2 24 18 6 40 0 L44 8 C28 16 22 30 24 44 Z"/>
    <circle cx="78" cy="56" r="22"/><path d="M58 56 C58 24 74 6 96 0 L100 8 C84 16 78 30 80 44 Z"/>
  </svg>
  <p class="abs">I began using your incentives two years ago to boost lead generation efforts. I have experienced a 63% increase in lead captures. And, even more importantly, my sales have increased as well. The ability to offer unlimited certificates and not having to pay for each certificate I give away is perhaps the best feature of the program, but having the flexibility to email or print certificates for my customers is also wonderful. I even use your html banners to automate my promotions right on my website!.</p>
  <div class="author abs">Dana R.</div>
  <div class="place abs">Fairhaven, TN</div>
</section>

<form class="bottom-form lead-form abs">
  <h2 class="display condensed-center">ENTER YOUR INFO</h2>
  <p>to be forwarded to our website for all the details and to receive samples in you email!</p>
  <label style="left:149px;top:158px">Name*</label>
  <div class="field" style="left:149px;top:192px;width:247px;height:29px"></div>
  <label style="left:478px;top:158px">Email*</label>
  <div class="field" style="left:478px;top:192px;width:247px;height:29px"></div>
  <label style="left:810px;top:158px">Phone*</label>
  <div class="field" style="left:810px;top:192px;width:248px;height:29px"></div>
  <div class="btn" style="left:497px;top:267px;width:201px;height:37px">Download Samples</div>
</form>

<footer class="footer abs">Copyright 2017 - 2025. Blue Willow Promo Group, Inc. - All Rights Revserved.</footer>

</body>
</html>
```